Modern & Aesthetic Electrician Sign Design for Work Vehicle

Modern and aesthetic signage design for an electricians work vehicle. Including already designed logo, mobile number, ABN, licensing number and services offered. Preference is black background, symmetric design with logo centred, services offered at bottom of sign in smaller size font. Mobile number readable and big enough to standout without being too large.

Industry/Entity Type

Electrician

Font styles to use
Serif
Sans Serif

Colors
000000
ffffff
ec1f27

Requirements
Must have
• Logo
• Services Offered
• Mobile Number
• ABN
• License Number
• Black background

```html
<!DOCTYPE html>
<html lang="en">
<head>
<meta charset="utf-8">
<title>Kestrel Electrical – Vehicle Signage Options</title>
<link href="https://fonts.googleapis.com/css2?family=Open+Sans:wght@300&family=Saira:wght@400;600;800&display=swap" rel="stylesheet">
<style>
  :root{
    --red:#ec1f27;
    --white:#ffffff;
    --black:#000000;
    --card-mid:#1d1d1d;
    --stage-top:#3a4143;
    --stage-bottom:#25292b;
  }
  html,body{margin:0;padding:0;overflow:hidden;}
  body{
    width:960px;height:1200px;position:relative;
    background:linear-gradient(160deg,var(--stage-top),var(--stage-bottom));
    font-family:"Saira",sans-serif;
  }
  .option-label{
    position:absolute;left:62px;
    font-family:"Open Sans",sans-serif;font-weight:300;font-size:28px;color:var(--white);
    transform:translate(-50%,-50%) rotate(-90deg);white-space:nowrap;
  }
  .sign{position:absolute;left:116px;width:728px;height:342px;display:block;}
  .sign text{font-family:"Saira",sans-serif;}
  .services{font-size:14px;fill:var(--white);font-weight:400;}
  .phone{font-size:60px;font-weight:800;fill:var(--white);}
  .credentials{font-size:20px;fill:var(--white);}
  .credentials .key{fill:var(--red);font-weight:800;}
  .credentials .val{font-weight:400;}
  .brand-name{fill:var(--red);font-weight:800;}
  .bullet{fill:var(--red);}
  .bullet-light{fill:var(--white);}
</style>
</head>
<body>

<div class="option-label" style="top:230px">option 1</div>
<div class="option-label" style="top:600px">option 2</div>
<div class="option-label" style="top:985px">option 3</div>

<!-- Option 1 -->
<svg class="sign" style="top:61px" viewBox="0 0 728 342" role="img" aria-label="Kestrel Electrical sign, option 1">
  <defs>
    <radialGradient id="bg1" cx="25%" cy="50%" r="75%">
      <stop offset="0" stop-color="var(--card-mid)"/><stop offset="1" stop-color="var(--black)"/>
    </radialGradient>
    <radialGradient id="band1" cx="70%" cy="50%" r="60%">
      <stop offset="0" stop-color="#f2131a"/><stop offset="1" stop-color="#9e0c11"/>
    </radialGradient>
  </defs>
  <rect width="728" height="342" fill="url(#bg1)"/>
  <polygon points="350,171 728,171 728,167 350,167" fill="var(--white)"/>
  <polygon class="service-band" points="350,42 728,42 728,165 350,165 304,104" fill="url(#band1)"/>
  <polygon points="304,104 350,167 356,171 350,171 302,106" fill="var(--white)"/>
  <g class="services">
    <text x="365" y="71"><tspan class="bullet-light">• </tspan>Lorem ipsum</text>
    <text x="365" y="97"><tspan class="bullet-light">• </tspan>Dolor sit</text>
    <text x="365" y="121"><tspan class="bullet-light">• </tspan>Consectetur</text>
    <text x="365" y="146"><tspan class="bullet-light">• </tspan>Consectetur</text>
    <text x="490" y="71"><tspan class="bullet-light">• </tspan>Ut enim ad</text>
    <text x="490" y="97"><tspan class="bullet-light">• </tspan>Duis aute</text>
    <text x="490" y="121"><tspan class="bullet-light">• </tspan>Laborum</text>
    <text x="490" y="146"><tspan class="bullet-light">• </tspan>Laborum</text>
    <text x="600" y="71"><tspan class="bullet-light">• </tspan>Lorem ipsum</text>
    <text x="600" y="97"><tspan class="bullet-light">• </tspan>Dolor sit</text>
    <text x="600" y="121"><tspan class="bullet-light">• </tspan>Consectetur</text>
    <text x="600" y="146"><tspan class="bullet-light">• </tspan>Consectetur</text>
  </g>
  <circle class="brand-circle" cx="168" cy="140" r="78" fill="none" stroke="var(--white)" stroke-width="6"/>
  <g class="brand-name">
    <text x="48" y="274" font-size="52" textLength="248" lengthAdjust="spacingAndGlyphs">KESTREL</text>
    <text x="50" y="296" font-size="16" textLength="244" lengthAdjust="spacing">ELECTRICAL</text>
  </g>
  <text class="phone" x="706" y="264" text-anchor="end">123-456-789</text>
  <text class="credentials" x="706" y="295" text-anchor="end"><tspan class="key">License Number</tspan><tspan class="val"> 01234  </tspan><tspan class="key">ABN</tspan><tspan class="val"> 01234</tspan></text>
</svg>

<!-- Option 2 -->
<svg class="sign" style="top:433px" viewBox="0 0 728 342" role="img" aria-label="Kestrel Electrical sign, option 2">
  <defs>
    <radialGradient id="bg2" cx="22%" cy="50%" r="70%">
      <stop offset="0" stop-color="var(--card-mid)"/><stop offset="1" stop-color="var(--black)"/>
    </radialGradient>
  </defs>
  <rect width="728" height="342" fill="url(#bg2)"/>
  <line x1="140" y1="0.5" x2="728" y2="0.5" stroke="var(--white)" stroke-width="1"/>
  <path class="swoosh" d="M140,0 C437,60 437,282 140,342 C400,282 400,60 140,0 Z" fill="var(--red)"/>
  <path d="M140,0 C395,62 395,280 140,342" fill="none" stroke="var(--white)" stroke-width="3"/>
  <g class="services">
    <text x="366" y="70"><tspan class="bullet">• </tspan>Lorem ipsum</text>
    <text x="366" y="94"><tspan class="bullet">• </tspan>Dolor sit</text>
    <text x="366" y="117"><tspan class="bullet">• </tspan>Consectetur</text>
    <text x="366" y="140"><tspan class="bullet">• </tspan>Consectetur</text>
    <text x="494" y="70"><tspan class="bullet">• </tspan>Ut enim ad</text>
    <text x="494" y="94"><tspan class="bullet">• </tspan>Duis aute</text>
    <text x="494" y="117"><tspan class="bullet">• </tspan>Laborum</text>
    <text x="494" y="140"><tspan class="bullet">• </tspan>Laborum</text>
    <text x="608" y="70"><tspan class="bullet">• </tspan>Lorem ipsum</text>
    <text x="608" y="94"><tspan class="bullet">• </tspan>Dolor sit</text>
    <text x="608" y="117"><tspan class="bullet">• </tspan>Consectetur</text>
    <text x="608" y="140"><tspan class="bullet">• </tspan>Consectetur</text>
  </g>
  <circle class="brand-circle" cx="162" cy="143" r="67" fill="none" stroke="var(--white)" stroke-width="5"/>
  <g class="brand-name">
    <text x="34" y="259" font-size="46" textLength="212" lengthAdjust="spacingAndGlyphs">KESTREL</text>
    <text x="35" y="278" font-size="14" textLength="210" lengthAdjust="spacing">ELECTRICAL</text>
  </g>
  <text class="phone" x="706" y="263" text-anchor="end">123-456-789</text>
  <text class="credentials" x="706" y="295" text-anchor="end"><tspan class="key">License Number</tspan><tspan class="val"> 01234  </tspan><tspan class="key">ABN</tspan><tspan class="val"> 01234</tspan></text>
</svg>

<!-- Option 3 -->
<svg class="sign" style="top:810px" viewBox="0 0 728 342" role="img" aria-label="Kestrel Electrical sign, option 3">
  <defs>
    <radialGradient id="bg3" cx="22%" cy="50%" r="70%">
      <stop offset="0" stop-color="var(--card-mid)"/><stop offset="1" stop-color="var(--black)"/>
    </radialGradient>
  </defs>
  <rect width="728" height="342" fill="url(#bg3)"/>
  <g class="stripes">
    <polygon points="313,0 318,0 275,198 270,198" fill="var(--white)"/>
    <polygon points="329,0 338,0 266,342 254,342" fill="var(--red)"/>
    <polygon points="312,179 316,179 280,342 276,342" fill="var(--white)"/>
  </g>
  <g class="services">
    <text x="366" y="70"><tspan class="bullet">• </tspan>Lorem ipsum</text>
    <text x="366" y="94"><tspan class="bullet">• </tspan>Dolor sit</text>
    <text x="366" y="117"><tspan class="bullet">• </tspan>Consectetur</text>
    <text x="366" y="140"><tspan class="bullet">• </tspan>Consectetur</text>
    <text x="494" y="70"><tspan class="bullet">• </tspan>Ut enim ad</text>
    <text x="494" y="94"><tspan class="bullet">• </tspan>Duis aute</text>
    <text x="494" y="117"><tspan class="bullet">• </tspan>Laborum</text>
    <text x="494" y="140"><tspan class="bullet">• </tspan>Laborum</text>
    <text x="608" y="70"><tspan class="bullet">• </tspan>Lorem ipsum</text>
    <text x="608" y="94"><tspan class="bullet">• </tspan>Dolor sit</text>
    <text x="608" y="117"><tspan class="bullet">• </tspan>Consectetur</text>
    <text x="608" y="140"><tspan class="bullet">• </tspan>Consectetur</text>
  </g>
  <circle class="brand-circle" cx="162" cy="143" r="67" fill="none" stroke="var(--white)" stroke-width="5"/>
  <g class="brand-name">
    <text x="34" y="259" font-size="46" textLength="212" lengthAdjust="spacingAndGlyphs">KESTREL</text>
    <text x="35" y="278" font-size="14" textLength="210" lengthAdjust="spacing">ELECTRICAL</text>
  </g>
  <text class="phone" x="706" y="263" text-anchor="end">123-456-789</text>
  <text class="credentials" x="706" y="295" text-anchor="end"><tspan class="key">License Number</tspan><tspan class="val"> 01234  </tspan><tspan class="key">ABN</tspan><tspan class="val"> 01234</tspan></text>
</svg>

</body>
</html>
```